Global Expert Network Firm needs business card design

We need business card design for a new company based in Seoul, South Korea called 'Corwell Insight Partners'. We recruit industry experts covering all countries and connect our client and recruited expert by phone, face-to-face meetings and etc. We are a global expert network firm that is focused on delivering high-quality experts to our clients throughout the world. Our clients include multinational corporations, global consulting firms, private equity firms, venture capital firms, asset management companies.
We have made new logo and please find attachment.(Please use new logo)
Target Market(s)
Global Consulting Firms, Investment Firms, Private Equity Firms, Venture Capital Firms.
Industry/Entity Type
Recruitment
Contact Information for Business Card
We need two Languages (English and Korean Version).
The front is Korean and the back is English version.
[The back] [English]
Company Name: Corwell Insight Partners, Inc.
CEO Name: Daniel Park
Address: #507, Hanbit Bldg, 82 Maebongsan-ro, Dobong-gu, Seoul, 01327, Korea
Tel. +82 2 718 4052
Fax. +82 2 864 1097
Mobile. +82 10 7264 8815
Email: daniel@corwellip.com
Web: www.corwellip.com
[The front] [Korean] => Described in same order as English version.
회사명: 코웰인사이트파트너스(주)
대표이사: 박도현
주소: 서울시 도봉구 매봉산로 82 한빛빌딩 507호
Tel. 02 718 4052
Fax. 02 864 1097
Mobile. 010 7264 8815
Web: www.corwellip.com
Look and feel
Each slider illustrates characteristics of the customer's brand and the style your logo design should communicate.

```html
<!DOCTYPE html>
<html lang="ko">
<head>
<meta charset="utf-8">
<title>Corwell Insight Partners — Business Cards</title>
<link rel="stylesheet" href="https://fonts.googleapis.com/css2?family=Noto+Sans+KR:wght@400;700&display=swap">
<style>
  :root {
    --bg: #d6d6d6;
    --navy: #232a6e;
    --navy-deep: #1b2157;
    --black: #1c1c1e;
    --white: #ffffff;
    --accent: #3aa0f0;
    --rule: rgba(255,255,255,0.45);
    --logo-box: #262f7a;
  }
  * { margin: 0; padding: 0; box-sizing: border-box; }
  html, body { width: 1200px; height: 800px; overflow: hidden; }
  body {
    background: var(--bg);
    font-family: "Noto Sans KR", Arial, sans-serif;
    display: flex; align-items: center; justify-content: center; gap: 40px;
  }
  .card {
    position: relative; width: 540px; height: 300px;
    color: var(--white); overflow: hidden;
    box-shadow: 0 6px 18px rgba(0,0,0,0.18);
  }
  .card--korean { background: linear-gradient(160deg, var(--navy) 0%, var(--navy-deep) 100%); }
  .card--english { background: var(--black); }
  .contact { position: absolute; left: 40px; top: 38px; }
  .contact__name { font-size: 17px; font-weight: 700; letter-spacing: 0.2px; }
  .contact__company { font-size: 11px; color: var(--accent); margin-top: 2px; margin-bottom: 12px; }
  .contact__row { display: flex; align-items: center; gap: 10px; font-size: 11px; line-height: 19px; }
  .contact__row svg { width: 13px; height: 13px; flex: none; }
  .contact__sep { margin: 0 8px; opacity: 0.8; }
  .contact__address { font-size: 11px; color: var(--accent); margin-top: 12px; line-height: 15px; }
  .divider { position: absolute; left: 0; right: 0; top: 212px; height: 1px; background: var(--rule); }
  .brand {
    position: absolute; right: 28px; top: 128px;
    display: flex; align-items: center; gap: 8px;
  }
  .brand__mark { width: 12px; height: 12px; background: var(--logo-box); border: 1px solid var(--rule); }
  .card--korean .brand__mark { background: var(--white); border: none; }
  .brand__name { font-size: 14px; font-weight: 400; letter-spacing: 1px; text-transform: uppercase; line-height: 1.3; width: 120px; }
</style>
</head>
<body>

<svg width="0" height="0" style="position:absolute">
  <defs>
    <symbol id="icon-phone" viewBox="0 0 16 16"><path d="M4 1.5l2.2 3-1.4 1.6c.8 1.8 2.3 3.3 4.1 4.1l1.6-1.4 3 2.2-1.3 2.5C7 13.5 2.5 9 2 3l2-1.5z" fill="currentColor"/></symbol>
    <symbol id="icon-fax" viewBox="0 0 16 16"><rect x="1.5" y="5" width="13" height="8" fill="none" stroke="currentColor" stroke-width="1.3"/><rect x="4" y="1.5" width="8" height="4" fill="none" stroke="currentColor" stroke-width="1.3"/><rect x="4" y="9" width="8" height="1.2" fill="currentColor"/></symbol>
    <symbol id="icon-globe" viewBox="0 0 16 16"><circle cx="8" cy="8" r="6.3" fill="none" stroke="currentColor" stroke-width="1.3"/><ellipse cx="8" cy="8" rx="2.8" ry="6.3" fill="none" stroke="currentColor" stroke-width="1.1"/><path d="M1.8 8h12.4M3 4.5h10M3 11.5h10" stroke="currentColor" stroke-width="1"/></symbol>
    <symbol id="icon-mail" viewBox="0 0 16 16"><rect x="1.5" y="3.5" width="13" height="9" fill="none" stroke="currentColor" stroke-width="1.3"/><path d="M1.5 3.5L8 9l6.5-5.5" fill="none" stroke="currentColor" stroke-width="1.3"/></symbol>
  </defs>
</svg>

<section class="card card--korean" lang="ko">
  <div class="contact">
    <p class="contact__name">박도현, 대표이사</p>
    <p class="contact__company">코웰인사이트파트너스(주)</p>
    <p class="contact__row"><svg><use href="#icon-phone"/></svg><span>+82 2 718 4052<span class="contact__sep">|</span>+82 10 7264 8815</span></p>
    <p class="contact__row"><svg><use href="#icon-fax"/></svg><span>+82 2 864 1097</span></p>
    <p class="contact__row"><svg><use href="#icon-globe"/></svg><span>www.corwellip.com</span></p>
    <p class="contact__row"><svg><use href="#icon-mail"/></svg><span>daniel@corwellip.com</span></p>
    <p class="contact__address">서울시 도봉구 매봉산로 82<br>한빛빌딩 507호</p>
  </div>
  <div class="brand">
    <span class="brand__mark"></span>
    <span class="brand__name">Corwell Insight Partners</span>
  </div>
  <div class="divider"></div>
</section>

<section class="card card--english" lang="en">
  <div class="contact">
    <p class="contact__name">DANIEL PARK, CEO</p>
    <p class="contact__company">Corwell Insight Partners, Inc.</p>
    <p class="contact__row"><svg><use href="#icon-phone"/></svg><span>+82 2 718 4052<span class="contact__sep">|</span>+82 10 7264 8815</span></p>
    <p class="contact__row"><svg><use href="#icon-fax"/></svg><span>+82 2 864 1097</span></p>
    <p class="contact__row"><svg><use href="#icon-globe"/></svg><span>www.corwellip.com</span></p>
    <p class="contact__row"><svg><use href="#icon-mail"/></svg><span>daniel@corwellip.com</span></p>
    <p class="contact__address">#507, HANBIT BLDG, 82 MAEBONGSAN-RO,<br>DOBONG-GU, SEOUL, 01327, KOREA</p>
  </div>
  <div class="brand">
    <span class="brand__mark"></span>
    <span class="brand__name">Corwell Insight Partners</span>
  </div>
  <div class="divider"></div>
</section>

</body>
</html>
```